Website for a online coaching platform

I would like a website designed with the same content the same as the one below:

https://www.corvel-ashby.com/

New practitioner Marek Tollvander

Target Market(s)

Injured athletes for treatment and medcal professionals for education

Industry/Entity Type

Professional sport and medical education

Coding

Coded - Design and coding required

Number of Pages Required

5+ page

Colors

Designer to choose colors to be used in the design.

Requirements
Must have
• Same amount and format of pages as sample website

```html
<!DOCTYPE html>
<html lang="en">
<head>
<meta charset="utf-8">
<title>MRK — Performance Rehabilitation Specialist</title>
<link href="https://fonts.googleapis.com/css2?family=Poppins:wght@400;500;600;700&display=swap" rel="stylesheet">
<style>
:root{
  --ink:#000;
  --paper:#fff;
  --muted:#444;
  --line:#d9d9d9;
  --card-line:#8a8a8a;
  --hero-a:#3b3530;
  --hero-b:#0c0b0a;
}
*{box-sizing:border-box;margin:0;padding:0}
html,body{width:1200px;height:4468px;overflow:hidden}
body{position:relative;background:var(--paper);color:var(--ink);font-family:'Poppins',sans-serif}
.abs{position:absolute}

/* header */
.brand{left:73px;top:24px;font-size:86px;font-weight:700;line-height:84px;letter-spacing:-2px}
.pill{height:40px;border:2px solid var(--ink);border-radius:20px;display:flex;align-items:center;font-size:14px;font-weight:600;gap:8px;padding:0 4px 0 16px;white-space:nowrap}
.pill-book{left:818px;top:29px;width:146px}
.pill-book .go{margin-left:auto;width:30px;height:30px;border-radius:50%;background:var(--ink);display:flex;align-items:center;justify-content:center;flex:none}
.pill-phone{left:976px;top:29px;width:164px;background:var(--ink);color:var(--paper);padding-left:4px}
.pill-phone .ic{width:30px;height:30px;border-radius:50%;background:var(--paper);display:flex;align-items:center;justify-content:center;flex:none}
.nav{left:378px;top:96px;display:flex;gap:17px;font-size:13.5px;font-weight:500;white-space:nowrap}
.nav a{color:var(--ink);text-decoration:none}

/* hero */
.hero{left:0;top:135px;width:1200px;height:697px;background:linear-gradient(100deg,var(--hero-a) 0%,#231f1c 45%,var(--hero-b) 100%)}
.hero-title{left:546px;top:326px;font-size:74px;font-weight:600;line-height:73px;color:var(--paper)}
.hero-sub{left:553px;top:565px;font-size:18px;color:var(--paper)}

/* shared headings */
.h2{font-weight:600;letter-spacing:-0.5px}
.rule{height:2px;background:currentColor;width:104px}

/* about */
.about-h{left:95px;top:966px;font-size:40px}
.about-rule{left:95px;top:1023px}
.about-lead{left:95px;top:1049px;width:460px;font-size:16.5px;font-weight:600;line-height:27px}
.about-body{left:95px;top:1108px;width:519px;font-size:13px;line-height:26.5px;color:var(--muted);text-align:justify}
.btn-dark{left:95px;top:1285px;width:169px;height:59px;border-radius:8px;background:var(--ink);color:var(--paper);font-size:15px;font-weight:600;display:flex;align-items:center;justify-content:center}
.about-frame{left:692px;top:940px;width:426px;height:409px;border:2px solid #333;border-radius:10px}
.about-photo{left:662px;top:973px;width:425px;height:409px;border-radius:8px;background:linear-gradient(135deg,#6d5a3a,#c9c0b0 45%,#b23a2f 85%)}

/* services */
.services{left:0;top:1497px;width:1200px;height:901px;background:var(--ink);color:var(--paper)}
.sec-title{width:1200px;left:0;text-align:center;font-size:38px}
.service-card{top:1731px;width:335px;height:428px;border:2px solid var(--card-line);border-radius:10px;color:var(--paper);text-align:center}
.service-card .photo{position:absolute;left:24px;top:26px;width:283px;height:196px;border-radius:4px}
.service-card h3{position:absolute;top:258px;left:0;width:100%;font-size:21px;font-weight:500;white-space:nowrap}
.service-card p{position:absolute;top:300px;left:24px;width:283px;font-size:14px;line-height:26.5px}
.service-card .more{position:absolute;left:89px;bottom:-25px;width:153px;height:47px;border:2px solid var(--card-line);border-radius:8px;background:var(--ink);font-size:16px;font-weight:500;display:flex;align-items:center;justify-content:center}
.dots{display:flex;gap:3px;align-items:center}
.dots span{width:7px;height:7px;border-radius:50%;border:1.5px solid currentColor}
.dots span:first-child{background:currentColor}

/* educator */
.edu-card{width:484px;height:415px;border:2px solid #e4e4e4;border-radius:8px;background:var(--paper)}
.edu-card .photo{position:absolute;left:15px;top:16px;width:452px;height:318px;border-radius:4px}
.edu-card .label{position:absolute;left:0;top:364px;width:100%;text-align:center;font-size:16px;font-weight:600}

/* contact */
.contact{left:0;top:3678px;width:1200px;height:709px;background:var(--ink);color:var(--paper)}
.contact-h{left:73px;top:3874px;font-size:42px;color:var(--paper)}
.contact-rule{left:73px;top:3936px;color:var(--paper)}
.contact-sub{left:73px;top:3970px;font-size:21px;color:var(--paper)}
.c-item{left:76px;display:flex;gap:14px;align-items:flex-start;font-size:16px;line-height:25px;color:var(--paper)}
.c-icon{width:36px;height:36px;border-radius:50%;background:var(--paper);display:flex;align-items:center;justify-content:center;flex:none}
.map-frame{left:685px;top:3815px;width:425px;height:412px;border:2px solid #ddd;border-radius:10px}
.map{left:654px;top:3848px;width:425px;height:409px;border-radius:6px;background:linear-gradient(135deg,#eef1f0,#e2e7e4 60%,#d4dfe6)}

/* footer */
.copy{left:71px;top:4416px;font-size:15.5px}
.social{top:4413px;width:30px;height:30px;border-radius:50%;background:var(--ink)}
</style>
</head>
<body>

<!-- header -->
<div class="abs brand">MRK</div>
<div class="abs pill pill-book">BOOK MRK
  <span class="go"><svg width="16" height="16" viewBox="0 0 16 16"><path d="M3 3l5 5-5 5M8 3l5 5-5 5" fill="none" stroke="#fff" stroke-width="2"/></svg></span>
</div>
<div class="abs pill pill-phone">
  <span class="ic"><svg width="16" height="16" viewBox="0 0 24 24"><path d="M6.6 10.8a15 15 0 006.6 6.6l2.2-2.2a1 1 0 011-.25 11.4 11.4 0 003.6.57 1 1 0 011 1V20a1 1 0 01-1 1A17 17 0 013 4a1 1 0 011-1h3.5a1 1 0 011 1c0 1.25.2 2.45.57 3.6a1 1 0 01-.25 1z" fill="#000"/></svg></span>987-654-3210
</div>
<nav class="abs nav">
  <a href="#" style="font-weight:700">HOME</a><a href="#">ABOUT US</a><a href="#">REHABILITATION SPECIALIST</a><a href="#">RESEARCHER</a><a href="#">EDUCATOR</a><a href="#">EVENTS CALENDAR</a><a href="#">CONTACT US</a>
</nav>

<!-- hero -->
<div class="abs hero" role="img" aria-label="Athlete training on a rowing machine in a dark gym"></div>
<h1 class="abs hero-title">PERFORMANCE<br>REHABILITATION<br>SPECIALIST</h1>
<p class="abs hero-sub">Expertise in Rehabilitation, Injury Prevention and Athletic Performance</p>

<!-- about -->
<h2 class="abs h2 about-h">ABOUT US</h2>
<div class="abs rule about-rule"></div>
<p class="abs about-lead">Marek Tollvander PhD MSc combines his roles as a sports physiotherapist,</p>
<p class="abs about-body">strength and conditioning coach, researcher, and educator through his work with individual athletes and elite teams across a spectrum of sports and disciplines. Currently, he is Head Elite Performance and Development in Veloria Clinic, Doha, Qatar and traveling internationally to work with athletes and professional clubs. He currently lives between Qatar and Ireland with his wife Sorcha and their 3 children Nora, Evan and Cillian.</p>
<div class="abs btn-dark">KNOW MORE</div>
<div class="abs about-frame"></div>
<div class="abs about-photo" role="img" aria-label="Woman training with suspension straps in a gym"></div>

<!-- services -->
<section class="abs services"></section>
<h2 class="abs h2 sec-title" style="top:1616px;color:#fff">REHABILITATION SERVICES</h2>
<div class="abs rule" style="left:548px;top:1678px;color:#fff"></div>

<div class="abs service-card" style="left:75px">
  <div class="photo" role="img" aria-label="Feet on a balance ball during ACL rehabilitation" style="background:linear-gradient(180deg,#c9c2b8,#3f6fb0)"></div>
  <h3>ACL REHABILITATION</h3>
  <p>Through his PhD and with the highly experienced ACL team at Veloria Clinic, Marek has been involved...</p>
  <div class="more">READ MORE</div>
</div>
<div class="abs service-card" style="left:432px">
  <div class="photo" role="img" aria-label="Athlete stretching legs on a clay track" style="background:linear-gradient(180deg,#d88a55,#c46a3b)"></div>
  <h3>ATHLETIC GROIN PAIN</h3>
  <p>Marek has published extensively in the area of athletic groin pain with numerous publications...</p>
  <div class="more">READ MORE</div>
</div>
<div class="abs service-card" style="left:799px">
  <div class="photo" role="img" aria-label="Athlete holding an injured upper arm" style="background:linear-gradient(135deg,#5e7c62,#2a2a2a)"></div>
  <h3>RECURRENT MUSCLE INJURY</h3>
  <p>While much of the focus in recurrent muscle injuries and chronic tendon problems focuses....</p>
  <div class="more">READ MORE</div>
</div>
<div class="abs dots" style="left:578px;top:2244px;color:#fff"><span></span><span></span><span></span><span></span><span></span></div>

<!-- educator -->
<h2 class="abs h2 sec-title" style="top:2504px">EDUCATOR</h2>
<div class="abs rule" style="left:548px;top:2566px"></div>

<div class="abs edu-card" style="left:106px;top:2630px">
  <div class="photo" role="img" aria-label="Coach guiding a woman lifting dumbbells" style="background:linear-gradient(135deg,#d8cfc4,#8a9aa8)"></div>
  <div class="label">IN PERSON COURSES</div>
</div>
<div class="abs edu-card" style="left:609px;top:2630px">
  <div class="photo" role="img" aria-label="Group workout session with fitness tracking overlay" style="background:linear-gradient(135deg,#2b2b2b,#6b6433)"></div>
  <div class="label">ONLINE COURSES</div>
</div>
<div class="abs edu-card" style="left:106px;top:3073px">
  <div class="photo" role="img" aria-label="Man doing lat pulldown in a gym" style="background:linear-gradient(135deg,#6b5a4a,#b8a24a)"></div>
  <div class="label">CPD RETREAT</div>
</div>
<div class="abs edu-card" style="left:609px;top:3073px">
  <div class="photo" role="img" aria-label="Studio microphone on a dark background" style="background:radial-gradient(circle at 65% 45%,#555,#0d0d0d 70%)"></div>
  <div class="label">RESOURCES</div>
</div>
<div class="abs dots" style="left:562px;top:3560px"><span></span><span></span><span></span><span></span><span></span></div>

<!-- contact -->
<section class="abs contact"></section>
<h2 class="abs h2 contact-h">CONTACT US</h2>
<div class="abs rule contact-rule"></div>
<p class="abs contact-sub">To work with Marek, contact him directly via:</p>
<div class="abs c-item" style="top:4040px">
  <span class="c-icon"><svg width="16" height="18" viewBox="0 0 24 24"><path d="M12 2a7 7 0 00-7 7c0 5 7 13 7 13s7-8 7-13a7 7 0 00-7-7zm0 9.5A2.5 2.5 0 1112 6.5a2.5 2.5 0 010 5z" fill="#000"/></svg></span>
  <span>Lorem ipsum ,Lorem ipsum ,<br>Lorem ipsum.</span>
</div>
<div class="abs c-item" style="top:4100px;align-items:center">
  <span class="c-icon"><svg width="16" height="16" viewBox="0 0 24 24"><path d="M6.6 10.8a15 15 0 006.6 6.6l2.2-2.2a1 1 0 011-.25 11.4 11.4 0 003.6.57 1 1 0 011 1V20a1 1 0 01-1 1A17 17 0 013 4a1 1 0 011-1h3.5a1 1 0 011 1c0 1.25.2 2.45.57 3.6a1 1 0 01-.25 1z" fill="#000"/></svg></span>
  <span>987-654-3210</span>
</div>
<div class="abs c-item" style="top:4150px;align-items:center">
  <span class="c-icon"><svg width="16" height="14" viewBox="0 0 24 18"><rect x="1" y="1" width="22" height="16" rx="2" fill="#000"/><path d="M2 3l10 7 10-7" fill="none" stroke="#fff" stroke-width="2"/></svg></span>
  <span>marektollvander@mailbox.com</span>
</div>
<div class="abs map-frame"></div>
<div class="abs map" role="img" aria-label="Street map showing the clinic location"></div>

<!-- footer -->
<p class="abs copy">Copyright © 2025 All Rights Reserved By Company Name</p>
<div class="abs social" style="left:1029px" role="img" aria-label="Social profile"></div>
<div class="abs social" style="left:1064px" role="img" aria-label="Social profile"></div>
<div class="abs social" style="left:1102px" role="img" aria-label="Social profile"></div>

</body>
</html>
```